Business card design for Plumbing and Gas fitting company

We need a business card design for our plumbing and gas fitting company using the company logo and director details. Design should be modern and eye-catching however kept reasonably simple. This design should be targeted at commercial businesses/work so professionalism is key.

Target Market(s)

Commercial/business

Industry/Entity Type

Plumbing

Contact Information for Business Card

Warwick Tane
Director
027 815 0937
warwick@harbourlinepipeworks.example
PO Box 8716
Palmerston North 4441

Font styles to use
Sans Serif

Requirements
Must have
• Logo
• Modern
• Kept simple
Nice to have
• Colour scheme based around logo

```html
<!DOCTYPE html>
<html lang="en">
<head>
<meta charset="utf-8">
<title>Harbourline Pipeworks – Business Card</title>
<link rel="stylesheet" href="https://fonts.googleapis.com/css2?family=Roboto:wght@400;500;700&display=swap">
<style>
  :root {
    --backdrop: #e6e6e6;
    --brand-blue: #0a6cb5;
    --brand-blue-deep: #0661a6;
    --brand-orange: #e8742a;
    --card-white: #f7f7f7;
    --ink: #2f2f2f;
    --ink-soft: #444444;
    --accent-pale-blue: #c9dfee;
    --accent-pale-peach: #f3dccb;
  }
  * { margin: 0; padding: 0; box-sizing: border-box; }
  html, body {
    width: 1200px; height: 576px; overflow: hidden;
    background: var(--backdrop);
    font-family: "Roboto", sans-serif;
  }
  .canvas { position: relative; width: 1200px; height: 576px; }

  .card {
    position: absolute;
    width: 484px; height: 292px;
    border-radius: 13px;
    overflow: hidden;
    box-shadow: 0 3px 6px rgba(0,0,0,0.18);
  }

  /* Back of card */
  .card-back {
    left: 82px; top: 139px;
    background: linear-gradient(180deg, var(--brand-blue) 0%, var(--brand-blue-deep) 100%);
    display: flex; align-items: center; justify-content: center;
  }
  .card-back .wordmark {
    display: flex; align-items: center; gap: 12px;
    color: #ffffff;
    font-weight: 700; font-size: 30px; letter-spacing: 0.2px;
  }
  .wordmark .dot {
    width: 22px; height: 22px; border-radius: 50%;
    background: #ffffff;
  }

  /* Front of card */
  .card-front {
    left: 603px; top: 138px;
    background: var(--card-white);
  }
  .card-front .wordmark {
    position: absolute; left: 25px; top: 44px;
    display: flex; align-items: center; gap: 10px;
    color: var(--brand-blue);
    font-weight: 700; font-size: 24px;
  }
  .card-front .wordmark .dot { width: 18px; height: 18px; background: var(--brand-orange); }

  .accent-decor {
    position: absolute; right: -60px; top: 40px;
    width: 250px; height: 250px; border-radius: 50%;
    background: linear-gradient(160deg, var(--accent-pale-blue) 0%, var(--accent-pale-peach) 100%);
    opacity: 0.75;
  }

  .person { position: absolute; left: 25px; top: 142px; }
  .person-name { color: var(--brand-blue); font-weight: 500; font-size: 21px; line-height: 1.2; }
  .person-role { color: var(--ink-soft); font-size: 11px; margin-top: 3px; }

  .contact { position: absolute; left: 25px; top: 312px; list-style: none; }
  .contact { top: 222px; }
  .contact li {
    display: flex; align-items: center; gap: 7px;
    color: var(--ink); font-size: 12px; line-height: 17px;
  }
  .contact li.address { margin-top: 3px; }
  .contact svg { width: 11px; height: 11px; fill: var(--brand-blue); flex: none; }
</style>
</head>
<body>
<main class="canvas">

  <section class="card card-back" aria-label="Card back">
    <div class="wordmark"><span class="dot"></span>Harbourline Pipeworks</div>
  </section>

  <section class="card card-front" aria-label="Card front">
    <div class="accent-decor" aria-hidden="true"></div>

    <div class="wordmark"><span class="dot"></span>Harbourline Pipeworks</div>

    <div class="person">
      <p class="person-name">Warwick Tane</p>
      <p class="person-role">Certified Plumber and Gasfitter</p>
    </div>

    <ul class="contact">
      <li>
        <svg viewBox="0 0 24 24" aria-hidden="true"><path d="M3 9c0-3 4-5 9-5s9 2 9 5v2h-5V9c-1-1-3-1.5-4-1.5S9 8 8 9v2H3z M6 13h12l2 7H4z"/></svg>
        027 815 0937
      </li>
      <li>
        <svg viewBox="0 0 24 24" aria-hidden="true"><path d="M2 5h20v14H2z M4 7v1l8 5 8-5V7l-8 5z" fill-rule="evenodd"/></svg>
        warwick@harbourlinepipeworks.example
      </li>
      <li class="address">PO Box 8716 Palmerston North 4441</li>
    </ul>
  </section>

</main>
</body>
</html>
```